Campaign website for Norvale Chamber of Delegates

I need a clean and easy to navigate web design for my campaign website. The theme of the campaign is fire. I need volunteers and visitors to quickly be able to find information about myself, our upcoming activities, where to vote, etc. The website should overall just be very user friendly. I would also like for there to be the option of viewing the website in spanish. Finally, I don't want the US Flag on the site.

Target Market(s)

Voters

Industry/Entity Type

Political

Coding

Coded - Design and coding required

Number of Pages Required

5+ page

Font styles to use
Serif

Colors
ffffff
ec1f27
000000
aaaaaa

Requirements
Must have
• I must have a donation link... the website that it routes to is www.givelantern.example/marisolfor42
• I also need a store to sell tshirts. I can send the tshirt design when you are ready to do the store.
• I have campaign platform issues that need to be included.
• I need information about the district included such as the map and demographical information which can be found here https://chamber.norvale.example/members/member-page/?district=42
• I need a volunteer button.
• I have uploaded a general draft of kind of what we are looking for. I will add more content, but I need to get the design started.
• I would like to make sure there is something encouraging people to donate on every page.
Nice to have
• It would be nice if my social media feed from facebook would be visible on the page.

```html
<!DOCTYPE html>
<html lang="en">
<head>
<meta charset="utf-8">
<title>Marisol Vance for State Delegate 42</title>
<link href="https://fonts.googleapis.com/css2?family=Playfair+Display:wght@400;700&family=Gruppo&family=Montserrat:wght@400;500;600&display=swap" rel="stylesheet">
<style>
:root{
  --red:#ec1f27;
  --black:#000000;
  --white:#ffffff;
  --grey:#aaaaaa;
  --panel:#1c1c1c;
  --serif:'Playfair Display',Georgia,serif;
  --thin:'Gruppo',sans-serif;
  --sans:'Montserrat',Arial,sans-serif;
}
*{box-sizing:border-box;margin:0;padding:0}
html,body{width:1200px;height:4218px;overflow:hidden;background:var(--black)}
body{position:relative;font-family:var(--serif);color:var(--white)}
.abs{position:absolute}
.btn{position:absolute;display:flex;align-items:center;justify-content:center;gap:10px;background:var(--red);color:var(--white);border-radius:26px;font-family:var(--serif);font-weight:700;text-decoration:none}
.btn .dot{width:18px;height:18px;border-radius:50%;background:var(--white);display:inline-flex;align-items:center;justify-content:center}
.btn .dot svg{width:10px;height:10px}
.wordmark{font-family:var(--serif);font-weight:400;color:var(--white);text-align:center;letter-spacing:2px;line-height:1}
.tagline{font-family:var(--serif);color:var(--white);text-align:center;letter-spacing:1px}
/* header */
.site-header{top:0;left:0;width:1200px;height:176px;background:var(--black)}
.main-nav a{position:absolute;top:128px;font-size:20px;color:var(--white);text-decoration:none;letter-spacing:.5px;white-space:nowrap}
.call{left:860px;top:36px;display:flex;gap:14px;align-items:center;font-size:14px;line-height:1.5}
.call .ring{width:40px;height:40px;border:2px solid var(--red);border-radius:50%;display:flex;align-items:center;justify-content:center}
/* hero */
.hero{top:176px;left:0;width:1200px;height:620px;background:linear-gradient(100deg,#2a1a14 0%,#5a2a20 30%,#3a2620 55%,#1c1410 100%)}
.hero-title{left:620px;top:520px;font-size:50px;font-weight:700;letter-spacing:1px}
/* behind fire */
.sec-title{font-family:var(--serif);text-align:center;width:1200px;left:0}
.radios{top:1004px;left:88px;width:1024px;display:flex;justify-content:space-between;font-size:17px}
.radios span{display:flex;align-items:center;gap:10px}
.radios i{width:18px;height:18px;border-radius:50%;background:var(--white);display:inline-flex;align-items:center;justify-content:center}
.field{position:absolute;top:1072px;width:226px;height:43px;background:var(--white);color:#888;font-size:13px;padding:0 12px;display:flex;align-items:center;justify-content:space-between}
.submit{top:1072px;left:870px;width:226px;height:43px;border-radius:0;font-family:var(--sans);font-weight:500;font-size:16px}
.rule{height:1px;background:#333;left:90px;width:1020px}
.red-h{color:var(--red);font-family:var(--serif);font-weight:400}
.body-copy{font-size:16px;line-height:34px;text-align:justify}
/* shop */
.shop-bg{top:1795px;left:0;width:1200px;height:680px;background:linear-gradient(180deg,#3d3d3d,#585858 50%,#2d2d2d)}
.product{position:absolute;width:250px;height:250px;border-radius:50%;background:#0d0d0d;border:4px solid var(--red);display:flex;flex-direction:column;align-items:center;justify-content:center;text-align:center}
.product .name{font-family:var(--thin);font-size:22px;font-weight:700}
.product .price{font-family:var(--thin);font-size:21px;font-weight:700;margin-top:4px}
.product .cart{font-family:var(--sans);font-size:13px;margin-top:8px}
.lead-list{left:90px;top:2680px;list-style:none;font-size:16px}
.lead-list li{display:flex;align-items:center;gap:20px;height:34px}
.lead-list i{width:16px;height:16px;border-radius:50%;background:var(--red);flex:none}
/* cards */
.card{position:absolute;top:3153px;width:328px;height:372px;background:var(--white);border-radius:20px;overflow:hidden;color:#222}
.card p{font-family:var(--sans);font-size:11px;line-height:24px;color:#333}
/* footer */
.footer-bg{top:3600px;left:0;width:1200px;height:618px;background:var(--panel)}
.contact{position:absolute;top:3888px;width:280px;text-align:center;font-size:17px;line-height:28px;white-space:nowrap}
.contact .ic{width:100px;height:100px;margin:0 auto 6px;border-radius:50%;border:3px solid var(--white);display:flex;align-items:center;justify-content:center}
.contact .ic span{width:84px;height:84px;border-radius:50%;background:var(--red);display:flex;align-items:center;justify-content:center}
.foot-nav{top:4076px;left:0;width:1200px;text-align:center;font-size:17px;line-height:24px}
.foot-nav a{color:var(--white);text-decoration:none;margin:0 10px}
.socials{top:4168px;left:530px;display:flex;gap:8px}
.socials span{width:30px;height:30px;border-radius:50%;border:2px solid var(--white)}
</style>
</head>
<body>

<!-- Header -->
<header class="abs site-header">
  <a class="btn" href="https://www.givelantern.example/marisolfor42" style="left:158px;top:35px;width:182px;height:50px;font-size:17px">Donate Now <span class="dot"><svg viewBox="0 0 10 10"><path d="M3 2l4 3-4 3" fill="none" stroke="#ec1f27" stroke-width="2"/></svg></span></a>
  <div class="abs wordmark" style="left:430px;top:48px;width:340px;font-size:74px">MARISOL</div>
  <div class="abs tagline" style="left:430px;top:128px;width:340px;font-size:14px">Vance for State Delegate 42</div>
  <div class="abs call"><span class="ring"><svg width="20" height="20" viewBox="0 0 24 24"><path d="M6 3l3 4-2 2c1 3 4 6 7 7l2-2 4 3-2 3C10 20 4 14 3 6z" fill="none" stroke="#ec1f27" stroke-width="2"/></svg></span><span>CALL US:<br>(555)-MAR-4-042</span></div>
  <nav class="main-nav">
    <a style="left:88px">Behind The Fire</a><a style="left:272px">Fuel</a><a style="left:354px">Issues</a>
    <a style="left:780px">Meet Marisol</a><a style="left:940px">Contact</a><a style="left:1060px">Shop</a>
  </nav>
</header>

<!-- Hero -->
<section class="abs hero" role="img" aria-label="Photo of the candidate in a red blazer applauding with supporters"></section>
<div class="abs wordmark" style="left:620px;top:370px;width:470px;font-size:104px">MARISOL</div>
<div class="abs tagline" style="left:620px;top:480px;width:470px;font-size:20px">Vance for State Delegate 42</div>
<div class="abs hero-title">HOME OF THE FIRE</div>
<svg class="abs" style="left:0;top:700px" width="1200" height="120" viewBox="0 0 1200 120">
  <path d="M0 96 Q600 20 1200 96 L1200 120 L0 120Z" fill="#000"/>
  <path d="M110 78 Q600 18 1090 78 Q600 30 110 78Z" fill="#ec1f27"/>
  <circle cx="600" cy="40" r="22" fill="#000"/>
  <path d="M600 22 C606 34 612 40 612 48 a12 12 0 0 1-24 0c0-8 6-14 12-26z" fill="#ec1f27"/>
</svg>

<!-- Behind the Fire -->
<h2 class="abs sec-title" style="top:868px;font-size:46px;font-weight:400">Behind the Fire</h2>
<p class="abs sec-title" style="top:944px;font-size:21px">What are important qualities you want from a leader?</p>
<div class="abs radios">
  <span><i><svg width="10" height="10" viewBox="0 0 10 10"><path d="M2 5l2 2 4-4" fill="none" stroke="#000" stroke-width="2"/></svg></i>Genuine and Honest</span>
  <span><i></i>Experience and Educated</span>
  <span><i></i>Commitment and Accountable</span>
  <span><i></i>Passionate and Inspiring</span>
</div>
<div class="field" style="left:103px">Full Name <span style="color:var(--red)">●</span></div>
<div class="field" style="left:359px">Phone Number <span style="color:var(--red)">✆</span></div>
<div class="field" style="left:614px">Email Address <span style="color:var(--red)">✉</span></div>
<a class="btn submit">➤ Submit</a>
<div class="abs rule" style="top:1195px"></div>

<!-- Why am I running -->
<svg class="abs" style="left:100px;top:1205px" width="405" height="575" viewBox="0 0 405 575" role="img" aria-label="Photo of the candidate seated on a bench in a marble hall">
  <defs><linearGradient id="g1" x1="0" y1="0" x2="0" y2="1"><stop offset="0" stop-color="#5a4a38"/><stop offset=".55" stop-color="#c9901e"/><stop offset="1" stop-color="#2a2018"/></linearGradient></defs>
  <path d="M160 0 C190 120 405 220 405 380 A200 195 0 0 1 5 380 C5 230 150 150 160 0Z" fill="url(#g1)"/>
</svg>
<h2 class="abs red-h" style="left:574px;top:1326px;font-size:46px">Why am I running?</h2>
<p class="abs body-copy" style="left:574px;top:1392px;width:536px">In the midst of political turmoil where millions are fighting for social equity, some lace up their shoes and march for justice while others infiltrate to change the very system that legally oppresses them; my life's work has consisted of both vital components in today's civil rights movement.</p>
<a class="btn" style="left:578px;top:1586px;width:184px;height:48px;font-size:18px">Volunteer <span class="dot"><svg viewBox="0 0 10 10"><path d="M3 2l4 3-4 3" fill="none" stroke="#ec1f27" stroke-width="2"/></svg></span></a>

<!-- Shop -->
<div class="abs shop-bg" role="img" aria-label="Greyscale photo of the state capitol directory wall"></div>
<svg class="abs" style="left:0;top:1790px" width="1200" height="690" viewBox="0 0 1200 690">
  <path d="M0 0 H1200 V20 Q500 20 0 90Z" fill="#000"/>
  <path d="M0 90 Q500 20 1200 20 L1200 30 Q520 40 0 110Z" fill="#ec1f27"/>
  <path d="M0 690 H1200 V600 Q700 680 0 690Z" fill="#000"/>
  <path d="M640 676 Q1000 640 1200 590 V606 Q1000 660 640 676Z" fill="#ec1f27"/>
</svg>
<h2 class="abs sec-title" style="top:1890px;font-size:38px;color:var(--red)">My Shop</h2>
<p class="abs" style="left:100px;top:1962px;width:1000px;text-align:center;font-size:16px;line-height:31px">Sed ut perspiciatis unde omnis iste natus error sit voluptatem accusantium doloremque laudantium, totam rem aperiam, eaque ipsa quae ab illo inventore veritatis et quasi architecto beatae vitae dicta sunt explicabo.</p>
<svg class="abs" style="left:0;top:2040px" width="1200" height="330" viewBox="0 0 1200 330">
  <g fill="#fff">
    <path d="M130 45 A140 140 0 0 1 320 40 A150 150 0 0 0 130 45Z"/><path d="M95 110 A145 145 0 0 0 140 300 A150 150 0 0 1 95 110Z"/><path d="M380 160 A150 150 0 0 1 270 315 A140 140 0 0 0 370 150Z"/>
    <path d="M486 45 A140 140 0 0 1 676 40 A150 150 0 0 0 486 45Z"/><path d="M451 110 A145 145 0 0 0 496 300 A150 150 0 0 1 451 110Z"/><path d="M736 160 A150 150 0 0 1 626 315 A140 140 0 0 0 726 150Z"/>
    <path d="M839 45 A140 140 0 0 1 1029 40 A150 150 0 0 0 839 45Z"/><path d="M804 110 A145 145 0 0 0 849 300 A150 150 0 0 1 804 110Z"/><path d="M1089 160 A150 150 0 0 1 979 315 A140 140 0 0 0 1079 150Z"/>
  </g>
</svg>
<div class="product" style="left:119px;top:2080px"><div class="name">Marisol for 42 T-Shirt</div><div class="price">Price: $25.00</div><div class="cart">Add to Cart</div></div>
<div class="product" style="left:475px;top:2080px"><div class="name">Marisol for 42 T-Shirt</div><div class="price">Price: $25.00</div><div class="cart">Add to Cart</div></div>
<div class="product" style="left:828px;top:2080px"><div class="name">Marisol for 42 T-Shirt</div><div class="price">Price: $25.00</div><div class="cart">Add to Cart</div></div>

<!-- Leadership -->
<h2 class="abs red-h" style="left:90px;top:2612px;font-size:46px">What leadership do I bring?</h2>
<ul class="abs lead-list">
  <li><i></i>Active and proud member of Alpha Lumen Sorority, Incorporated.</li>
  <li><i></i>President of the Norvale Criminal Bar Association</li>
  <li><i></i>Board Member Civic Lawyers Section of the State Bar of Norvale</li>
  <li><i></i>Former Board Member of the Youth Harbor Club</li>
  <li><i></i>Former Board Member for Cityline Care Services</li>
</ul>
<a class="btn" style="left:96px;top:2870px;width:180px;height:48px;font-size:18px">Read More <span class="dot"><svg viewBox="0 0 10 10"><path d="M3 2l4 3-4 3" fill="none" stroke="#ec1f27" stroke-width="2"/></svg></span></a>
<svg class="abs" style="left:688px;top:2490px" width="407" height="570" viewBox="0 0 407 570" role="img" aria-label="Portrait of the candidate in a black coat outside the capitol">
  <defs><linearGradient id="g2" x1="0" y1="0" x2="0" y2="1"><stop offset="0" stop-color="#6d6458"/><stop offset=".5" stop-color="#3e3a36"/><stop offset="1" stop-color="#141414"/></linearGradient></defs>
  <path d="M160 0 C190 120 407 220 407 375 A202 195 0 0 1 3 375 C3 230 150 150 160 0Z" fill="url(#g2)"/>
</svg>
<div class="abs rule" style="top:3077px"></div>

<!-- Cards -->
<article class="card" style="left:90px">
  <div class="abs" style="left:18px;top:42px;width:34px;height:54px;background:#000"></div>
  <div class="abs" style="left:60px;top:40px;font-family:var(--sans);font-size:11px;line-height:18px;color:#333">Marisol Vance for District 42<br>@marisolfor42<br><span style="color:#888;font-size:9px">Like · Reply · 1 · 10 Oct at 22:18</span></div>
  <div class="abs" style="left:18px;top:118px;width:290px;height:146px;background:linear-gradient(#8ea06a,#4c5a6a)" role="img" aria-label="Photo of a campaign tent event"></div>
  <p class="abs" style="left:18px;top:276px;width:290px">Lorem ipsum dolor sit amet, consectetur adipiscing elit, sed do eiusmod tempor incididunt ut labore et dolore magna aliqua.</p>
</article>
<div class="card" style="left:436px;background:#f0e44c" role="img" aria-label="Map of District 42"></div>
<article class="card" style="left:782px">
  <div class="abs" style="left:18px;top:18px;width:290px;height:156px;background:linear-gradient(#b8c4d0,#6a7a5a)" role="img" aria-label="Photo of supporters at a campaign tent"></div>
  <h3 class="abs" style="left:18px;top:188px;font-family:var(--sans);font-weight:500;font-size:26px;color:var(--red)">Campaign Platform</h3>
  <p class="abs" style="left:18px;top:232px;width:290px">Lorem ipsum dolor sit amet, consectetur adipiscing elit, sed do eiusmod tempor incididunt ut labore et dolore magna aliqua. Lorem ipsum dolor sit amet, consectetur adipiscing elit, sed do eiusmod tempor incididunt ut labore et dolore magna aliqua.</p>
</article>

<!-- Footer -->
<div class="abs footer-bg"></div>
<svg class="abs" style="left:0;top:3590px" width="1200" height="120" viewBox="0 0 1200 120">
  <path d="M0 0 H1200 V20 Q600 90 0 20Z" fill="#000"/>
  <path d="M120 56 Q600 120 1080 56 Q600 104 120 56Z" fill="#ec1f27"/>
  <circle cx="600" cy="92" r="22" fill="#1c1c1c"/>
  <path d="M600 74 C606 86 612 92 612 100 a12 12 0 0 1-24 0c0-8 6-14 12-26z" fill="#ec1f27"/>
</svg>
<div class="abs wordmark" style="left:420px;top:3748px;width:360px;font-size:84px">MARISOL</div>
<div class="abs tagline" style="left:420px;top:3842px;width:360px;font-size:16px">Vance for State Delegate 42</div>

<div class="contact" style="left:136px"><div class="ic"><span><svg width="40" height="40" viewBox="0 0 24 24"><path d="M12 2a7 7 0 0 0-7 7c0 5 7 13 7 13s7-8 7-13a7 7 0 0 0-7-7z" fill="none" stroke="#fff" stroke-width="1.5"/><circle cx="12" cy="9" r="2.5" fill="none" stroke="#fff" stroke-width="1.5"/></svg></span></div>P.O. Box 40412<br>Norvale City, NV 00042</div>
<div class="contact" style="left:440px"><div class="ic"><span><svg width="40" height="40" viewBox="0 0 24 24"><path d="M6 3l3 4-2 2c1 3 4 6 7 7l2-2 4 3-2 3C10 20 4 14 3 6z" fill="none" stroke="#fff" stroke-width="1.5"/></svg></span></div>Phone:<br>(555)-MAR-4-042</div>
<div class="contact" style="left:744px"><div class="ic"><span><svg width="42" height="42" viewBox="0 0 24 24"><rect x="3" y="6" width="18" height="12" fill="none" stroke="#fff" stroke-width="1.5"/><path d="M3 6l9 7 9-7" fill="none" stroke="#fff" stroke-width="1.5"/></svg></span></div>Email:<br>info@marisolfor42.example</div>

<nav class="abs foot-nav"><a>Behind The Fire</a>|<a>Meet Marisol</a>|<a>Issues</a>|<a>Fuel</a>|<a>Contact</a>|<a>Shop</a></nav>
<p class="abs sec-title" style="top:4120px;font-size:16px">© Marisol For 42 2019. All rights reserved</p>
<div class="abs socials"><span aria-label="Social profile"></span><span aria-label="Social profile"></span><span aria-label="Social profile"></span><span aria-label="Social profile"></span></div>

</body>
</html>
```